Business Card and Stationary Design

After the successful redesign of our logo we are wanting to follow suite and create a new business card and stationary design!

New Logo is attached, information required on the business card should contain a mixture of the following but layout/arrangement is up to the designer.

Happy if the national provider number and abn are on the back, and happy for them to be smaller than the rest.

I am also happy to receive single sided or weird and wonderful designs.

Name
Title
National Provider Number 7192
ABN 53 614 289 117
Level 1, 214 Garrow Street
Harlow Vale NSW 2291
Ph: 1300 587 902
Mobile: 0438 761 205
name@ironquillbuild.com.au
www.ironquillbuild.com.au

Target Market(s)

Professionals, Peers, Students, Suppliers...

Industry/Entity Type

Construction

Contact Information for Business Card

Listed in project description

Font styles to use
Other font styles liked:
• Century Gothic

Colors
0455a3
3176b5
ffffff

Requirements
Must have
• Professional Design, same color scheme as our logo
Nice to have
• Something that sets our apart from everyone else would be fantastic, open to size and shape and layout options, as long as they present professionally.
• Open to raised/embossed text, alternative materials, custom sizes, clear material
Should not have
• The color orange

```html
<!DOCTYPE html>
<html lang="en">
<head>
<meta charset="utf-8">
<title>Iron Quill Build – Business Card</title>
<link rel="stylesheet" href="https://fonts.googleapis.com/css2?family=Questrial&display=swap">
<style>
  :root {
    --navy: #1f3a7a;
    --grey-text: #6d6d6d;
    --strip: #efefef;
    --paper: #ffffff;
    --backdrop: #e9e6e1;
  }
  * { margin: 0; padding: 0; box-sizing: border-box; }
  html, body { width: 1200px; height: 1200px; overflow: hidden; }
  body {
    background: var(--backdrop);
    font-family: "Questrial", "Century Gothic", sans-serif;
    position: relative;
  }
  .card {
    position: absolute;
    left: 317px;
    width: 538px;
    height: 309px;
    background: var(--paper);
    box-shadow: 0 10px 14px -8px rgba(0,0,0,0.35);
    overflow: hidden;
  }
  .card--front { top: 286px; }
  .card--back { top: 664px; }

  .wordmark {
    position: absolute;
    display: flex;
    align-items: center;
    gap: 8px;
    color: var(--navy);
    white-space: nowrap;
    transform: translate(-50%, -50%);
  }
  .wordmark__square { width: 14px; height: 14px; background: var(--navy); }
  .card--front .wordmark { left: 269px; top: 152px; font-size: 30px; }
  .card--back .wordmark { left: 147px; top: 160px; font-size: 24px; }

  .company-details {
    position: absolute;
    left: 0; right: 0; top: 260px;
    text-align: center;
    font-size: 12px;
    color: var(--grey-text);
    white-space: nowrap;
  }
  .provider-band {
    position: absolute;
    left: 0; right: 0; bottom: 0;
    height: 26px;
    background: var(--navy);
    color: var(--paper);
    font-size: 12.5px;
    line-height: 26px;
    text-align: center;
  }

  .side-strip {
    position: absolute;
    left: 284px; top: 14px;
    width: 61px; height: 280px;
    background: var(--strip);
    box-shadow: -4px 0 6px -3px rgba(0,0,0,0.25);
  }
  .person { position: absolute; left: 314px; top: 94px; }
  .person__name { font-size: 18px; color: var(--navy); line-height: 1.2; }
  .person__title { font-size: 14px; color: var(--grey-text); margin-top: 2px; }

  .contact-list {
    position: absolute;
    left: 295px; top: 155px;
    list-style: none;
  }
  .contact-list li {
    display: flex;
    align-items: center;
    gap: 6px;
    height: 20px;
    font-size: 12.5px;
    color: var(--grey-text);
    white-space: nowrap;
  }
  .contact-list svg { width: 14px; height: 14px; flex: none; }
</style>
</head>
<body>

<section class="card card--front" aria-label="Card front">
  <div class="wordmark"><span class="wordmark__square"></span>Iron Quill Build</div>
  <p class="company-details">ABN&nbsp; 53 614 289 117 Level 1, 214 Garrow Street Harlow Vale NSW 2291</p>
  <div class="provider-band">National Provider Number 7192</div>
</section>

<section class="card card--back" aria-label="Card back">
  <div class="wordmark"><span class="wordmark__square"></span>Iron Quill Build</div>
  <div class="side-strip"></div>
  <div class="person">
    <p class="person__name">Daniel Reeve</p>
    <p class="person__title">Title</p>
  </div>
  <ul class="contact-list">
    <li>
      <svg viewBox="0 0 14 14"><circle cx="7" cy="7" r="7" fill="var(--navy)"/><path d="M4 5.5c0-1 1.3-1.5 3-1.5s3 .5 3 1.5v.6H8.6v-.6H5.4v.6H4zM4.6 7h4.8l.6 3H4z" fill="#fff"/></svg>
      01300 587 902
    </li>
    <li>
      <svg viewBox="0 0 14 14"><circle cx="7" cy="7" r="7" fill="var(--navy)"/><rect x="5" y="3.2" width="4" height="7.6" rx="0.8" fill="#fff"/></svg>
      00438 761 205
    </li>
    <li>
      <svg viewBox="0 0 14 14"><circle cx="7" cy="7" r="7" fill="var(--navy)"/><rect x="3.6" y="4.6" width="6.8" height="4.8" fill="#fff"/><path d="M3.6 4.6L7 7.3l3.4-2.7" stroke="var(--navy)" stroke-width="0.8" fill="none"/></svg>
      name@ironquillbuild.com.au
    </li>
    <li>
      <svg viewBox="0 0 14 14"><circle cx="7" cy="7" r="7" fill="var(--navy)"/><circle cx="7" cy="7" r="3.4" stroke="#fff" stroke-width="0.9" fill="none"/><path d="M3.6 7h6.8M7 3.6v6.8" stroke="#fff" stroke-width="0.8"/></svg>
      0ironquillbuild.com.au
    </li>
  </ul>
</section>

</body>
</html>
```